ROLLFAST FITNESSRoll Out, A UNIQUE CONCIERGE MOBILE SERVICE LAUNCHING in SOUTH FLORIDA

I AM LOOKING TO ATTRACT LEADS FOR CONVERSION WHILE BRINGING OUR SERVICE TO LIFE IN THERE HANDS. WE SERVICE A VERY HIGHLY AFFLUENT CROWD. I would like those on a 5 x 7 two sided card

Target Market(s)

AFFLUENT

Industry/Entity Type

HEALTH AND FITNESS

Font styles to use
Other font styles liked:
• POPINS MED

Colors
0054AA
0677BA
7BADD7
CADEEF
E8F1F8
FFF300
FFF600
FEFA6F
FFFEC7
FFFEE8

Requirements
Must have
• space for postage I INCLUDED CONTENT
Nice to have
• CLASSY FUN LOOK
Should not have
• DULLNESs

```html
<!DOCTYPE html>
<html lang="en">
<head>
<meta charset="utf-8">
<title>SkyBend Fitness – Postcard Front and Back</title>
<link rel="stylesheet" href="https://fonts.googleapis.com/css2?family=Poppins:wght@400;500;600;700;800&display=swap">
<style>
  :root {
    --page-bg: #e6e7ea;
    --card-white: #ffffff;
    --brand-cyan: #6acbd9;
    --brand-yellow: #fff200;
    --ink-dark: #3a3a3c;
    --ink-mid: #4a4a4d;
    --globe-dark: #3d3d40;
    --photo-warm: #b9a89a;
    --photo-cool: #8f959c;
    --photo-sky: #d6dbe0;
  }
  html, body {
    margin: 0;
    padding: 0;
    width: 1200px;
    height: 900px;
    overflow: hidden;
    background: var(--page-bg);
    font-family: "Poppins", sans-serif;
  }
  .canvas {
    position: relative;
    width: 1200px;
    height: 900px;
  }
  .postcard {
    position: absolute;
    width: 560px;
    height: 400px;
    background: var(--card-white);
    box-shadow: 0 6px 18px rgba(0,0,0,0.12);
  }
  .postcard--front { left: 40px; top: 50px; }
  .postcard--back  { left: 600px; top: 450px; }
  .postcard svg { display: block; width: 560px; height: 400px; }
  .brand-name { font-family: "Poppins", sans-serif; font-weight: 700; fill: var(--brand-cyan); letter-spacing: 0.5px; }
  .headline { font-family: "Poppins", sans-serif; font-weight: 700; fill: var(--ink-dark); }
  .subline { font-family: "Poppins", sans-serif; font-weight: 400; fill: var(--ink-mid); }
  .url-text { font-family: "Poppins", sans-serif; font-weight: 500; fill: #ffffff; }
  .cta-text { font-family: "Poppins", sans-serif; font-weight: 400; fill: var(--ink-mid); }
  .cta-strong { font-family: "Poppins", sans-serif; font-weight: 700; fill: var(--ink-dark); }
</style>
</head>
<body>
<main class="canvas">

  <!-- Front side -->
  <section class="postcard postcard--front">
    <svg viewBox="0 0 560 400" xmlns="http://www.w3.org/2000/svg">
      <defs>
        <linearGradient id="frontPhotoTone" x1="0" y1="0" x2="1" y2="1">
          <stop offset="0" stop-color="var(--photo-sky)"/>
          <stop offset="0.5" stop-color="var(--photo-cool)"/>
          <stop offset="1" stop-color="var(--photo-warm)"/>
        </linearGradient>
        <linearGradient id="insetPhotoTone" x1="0" y1="0" x2="0" y2="1">
          <stop offset="0" stop-color="var(--photo-sky)"/>
          <stop offset="1" stop-color="var(--photo-cool)"/>
        </linearGradient>
      </defs>

      <g class="hero-photo" role="img" aria-label="Photo: client training with resistance bands beside the branded fitness truck on a rooftop">
        <polygon points="150,0 560,0 560,300 200,400 150,400" fill="url(#frontPhotoTone)"/>
      </g>

      <polygon class="accent-yellow-band" points="560,280 560,318 250,400 180,400" fill="var(--brand-yellow)"/>
      <polygon class="accent-white-corner" points="560,322 560,400 265,400" fill="var(--card-white)"/>
      <line x1="560" y1="320" x2="258" y2="400" stroke="var(--brand-cyan)" stroke-width="3"/>

      <path class="text-panel" d="M0 0 L200 0 L298 146 Q310 166 296 186 L150 400 L0 400 Z" fill="var(--card-white)"/>

      <polygon class="accent-cyan-corner" points="125,0 235,0 205,58" fill="var(--brand-cyan)"/>
      <polygon class="accent-yellow-sliver" points="205,58 235,0 250,0 224,92" fill="var(--brand-yellow)"/>

      <g class="inset-photo">
        <circle cx="268" cy="290" r="52" fill="var(--card-white)"/>
        <circle cx="268" cy="290" r="47" fill="url(#insetPhotoTone)" role="img" aria-label="Photo: branded fitness truck with training equipment"/>
        <circle cx="268" cy="290" r="49" fill="none" stroke="var(--brand-yellow)" stroke-width="2"/>
      </g>

      <text class="brand-name" x="38" y="98" font-size="24">SKYBEND FITNESS</text>

      <text class="headline" font-size="20">
        <tspan x="38" y="160">GET FIT ON</tspan>
        <tspan x="38" y="185">YOUR SCHEDULE,</tspan>
        <tspan x="38" y="210">ANYWHERE, ANYTIME</tspan>
      </text>

      <text class="subline" font-size="9.5">
        <tspan x="38" y="232">The Ultimate Mobile Concierge Fitness</tspan>
        <tspan x="38" y="245">Service for Health, Golf, Tennis,</tspan>
        <tspan x="38" y="258">Flexibility, Strength, and Agility</tspan>
      </text>

      <g class="website-pill">
        <rect x="44" y="273" width="168" height="22" rx="11" fill="var(--brand-cyan)"/>
        <circle cx="46" cy="284" r="13" fill="var(--card-white)"/>
        <circle cx="46" cy="284" r="10.5" fill="var(--globe-dark)"/>
        <g fill="none" stroke="#ffffff" stroke-width="1">
          <circle cx="46" cy="284" r="6"/>
          <ellipse cx="46" cy="284" rx="2.6" ry="6"/>
          <line x1="40" y1="284" x2="52" y2="284"/>
          <line x1="41" y1="281" x2="51" y2="281"/>
          <line x1="41" y1="287" x2="51" y2="287"/>
        </g>
        <text class="url-text" x="64" y="288.5" font-size="12">skybendfitness.com</text>
      </g>

      <g class="chevron-row" fill="none" stroke-width="4.5" stroke-linejoin="miter">
        <polyline points="44,318 58,330 44,342" stroke="var(--brand-cyan)"/>
        <polyline points="60,318 74,330 60,342" stroke="var(--brand-yellow)"/>
        <polyline points="76,318 90,330 76,342" stroke="var(--brand-cyan)"/>
        <polyline points="92,318 106,330 92,342" stroke="var(--brand-yellow)"/>
        <polyline points="108,318 122,330 108,342" stroke="var(--brand-cyan)"/>
        <polyline points="124,318 138,330 124,342" stroke="var(--brand-yellow)"/>
        <polyline points="140,318 154,330 140,342" stroke="var(--brand-cyan)"/>
      </g>
    </svg>
  </section>

  <!-- Back side -->
  <section class="postcard postcard--back">
    <svg viewBox="0 0 560 400" xmlns="http://www.w3.org/2000/svg">
      <defs>
        <linearGradient id="backPhotoTone" x1="0" y1="0" x2="1" y2="1">
          <stop offset="0" stop-color="var(--photo-sky)"/>
          <stop offset="0.45" stop-color="var(--photo-cool)"/>
          <stop offset="1" stop-color="var(--photo-warm)"/>
        </linearGradient>
      </defs>

      <g class="hero-photo" role="img" aria-label="Photo: small group class training with suspension straps and bands beside the branded fitness truck">
        <rect x="0" y="0" width="560" height="400" fill="url(#backPhotoTone)"/>
      </g>

      <polygon class="accent-yellow-band" points="560,245 560,400 0,400 0,340" fill="var(--brand-yellow)"/>
      <polygon class="cta-strip" points="0,356 430,312 372,400 0,400" fill="var(--card-white)"/>
      <line x1="0" y1="353" x2="432" y2="309" stroke="var(--brand-cyan)" stroke-width="3"/>

      <path class="text-panel" d="M290 0 L560 0 L560 232 L512 278 Q496 294 478 282 L238 132 Q220 120 230 102 L286 6 Z" fill="var(--card-white)"/>

      <text class="brand-name" x="530" y="68" font-size="24" text-anchor="end">SKYBEND FITNESS</text>

      <text class="headline" font-size="16.5" text-anchor="end">
        <tspan x="530" y="108">TRANSFORM YOUR BODY</tspan>
        <tspan x="530" y="130">AND YOUR GAME WITH</tspan>
        <tspan x="530" y="152">SKYBEND FITNESS</tspan>
      </text>

      <text class="subline" font-size="9.5" text-anchor="end">
        <tspan x="530" y="176">The Ultimate Mobile Concierge</tspan>
        <tspan x="530" y="189">Fitness Service for Health, Golf,</tspan>
        <tspan x="530" y="202">Tennis, Flexibility,</tspan>
        <tspan x="530" y="215">Strength, and Agility</tspan>
      </text>

      <g class="chevron-row" fill="none" stroke-width="4.5" stroke-linejoin="miter">
        <polyline points="500,232 486,244 500,256" stroke="var(--brand-cyan)"/>
        <polyline points="514,232 500,244 514,256" stroke="var(--brand-yellow)"/>
        <polyline points="528,232 514,244 528,256" stroke="var(--brand-cyan)"/>
      </g>

      <g class="cta-copy" transform="rotate(-5.8 14 384)">
        <text class="cta-text" x="14" y="372" font-size="9.5">Conclusion: Get Started with SkyBend Fitness Today</text>
        <text class="cta-strong" x="14" y="386" font-size="10">FOR FREE CONSULTAION AND ASSESMENT GO TO:</text>
      </g>

      <g class="website-pill">
        <rect x="392" y="352" width="158" height="22" rx="11" fill="var(--brand-cyan)"/>
        <circle cx="394" cy="363" r="13" fill="var(--card-white)"/>
        <circle cx="394" cy="363" r="10.5" fill="var(--globe-dark)"/>
        <g fill="none" stroke="#ffffff" stroke-width="1">
          <circle cx="394" cy="363" r="6"/>
          <ellipse cx="394" cy="363" rx="2.6" ry="6"/>
          <line x1="388" y1="363" x2="400" y2="363"/>
          <line x1="389" y1="360" x2="399" y2="360"/>
          <line x1="389" y1="366" x2="399" y2="366"/>
        </g>
        <text class="url-text" x="411" y="367.5" font-size="11.5">skybendfitness.com</text>
      </g>
    </svg>
  </section>

</main>
</body>
</html>
```